Mar-wick Sky Harbor Custom Brokers Limited

The Company deals with:
shipping
logistic
imports
Export
customs clearance (customs broker services); and
customers can shop online and we take care of the shipment from the United States of America to Jamaica.
(we offer freight forwarding services from USA to Kingston Jamaica
Our tagline is : Creating Waves in the Logistic Industry.
Address: Shop 9 Birchfield Trade Centre, 227-229 Welland Avenue Kingston 8, Jamaica West Indies Telephone: (876)555-0193
Example of what we required can be seem: www.swiftparcelhubexample.com

```html
<!DOCTYPE html>
<html lang="en">
<head>
<meta charset="utf-8">
<title>Mar-wick Sky Harbor Custom Brokers — Home Page Concepts</title>
<link rel="stylesheet" href="https://fonts.googleapis.com/css2?family=Montserrat:wght@400;500;600;700&family=Arimo:wght@400;700&display=swap">
<style>
:root{
  --navy:#13264c;
  --navy-deep:#112a55;
  --orange:#e9a114;
  --board:#1b1b1b;
  --text:#4a4a4a;
  --line:#d6d9de;
  --white:#ffffff;
}
*{box-sizing:border-box;margin:0;padding:0}
html,body{width:769px;height:1200px;overflow:hidden;background:var(--board)}
body{position:relative;font-family:"Arimo",Arial,sans-serif;color:var(--text)}
.page{position:absolute;top:20px;width:359px;background:var(--white);overflow:hidden}
.page--a{left:21px}
.page--b{left:390px}
section,header,footer{position:relative;width:100%}
.abs{position:absolute}
.accent{color:var(--orange)}

/* header */
.site-header{height:43px;background:var(--white)}
.brand{left:28px;top:5px;width:70px;text-align:center}
.brand__mark{display:flex;align-items:center;justify-content:center;gap:3px}
.brand__dot{width:9px;height:9px;border-radius:50%;background:var(--orange);flex:none}
.brand__name{font-family:"Montserrat",sans-serif;font-weight:700;font-size:5px;color:var(--navy);white-space:nowrap}
.brand__sub{font-size:2.6px;letter-spacing:.6px;color:var(--navy);margin-top:2px}
.brand__addr{left:22px;top:29px;width:82px;font-size:3.1px;line-height:5.6px;color:#222;text-align:center}
.btn{display:flex;align-items:center;justify-content:center;border-radius:9px;font-family:"Montserrat",sans-serif;font-weight:500;color:var(--white);white-space:nowrap}
.btn--navy{background:var(--navy)}
.btn--orange{background:var(--orange)}
.get-started{left:193px;top:8px;width:42px;height:14px;font-size:4.2px}
.call{left:242px;top:6px;display:flex;align-items:center;gap:3px;font-size:5px;color:var(--orange);white-space:nowrap}
.ico-circle{width:16px;height:16px;border-radius:50%;background:var(--orange);display:flex;align-items:center;justify-content:center;flex:none}
.nav{left:168px;top:30px;display:flex;gap:15px;font-family:"Montserrat",sans-serif;font-size:4px;font-weight:500;color:#222;white-space:nowrap}
.nav .is-active{color:var(--orange)}

/* hero */
.hero{height:187px;background:linear-gradient(90deg,#3a4a63 0%,#8b5a34 18%,#c98d47 40%,#b87a48 62%,#6b4a3a 80%,#c7b6a4 100%)}
.hero__shade{inset:0;background:linear-gradient(180deg,rgba(255,255,255,.12),rgba(0,0,0,.05) 60%,rgba(0,0,0,.25))}
.hero__title{left:0;right:0;top:73px;text-align:center;font-family:"Montserrat",sans-serif;font-weight:600;font-size:12.5px;color:var(--navy);letter-spacing:.3px}
.hero__sub{left:0;right:0;top:95px;text-align:center;font-family:"Montserrat",sans-serif;font-weight:500;font-size:7.4px;color:var(--white)}
.hero__btn{left:151px;top:113px;width:58px;height:17px;font-size:4.6px}

/* welcome */
.welcome{height:154px}
.welcome__kicker{left:33px;top:20px;font-family:"Montserrat",sans-serif;font-weight:600;font-size:5.4px;color:#111}
.welcome__title{left:33px;top:27px;font-family:"Montserrat",sans-serif;font-weight:600;font-size:8.2px;color:var(--orange);white-space:nowrap}
.welcome__text{left:33px;top:46px;width:137px;font-size:3.7px;line-height:8.2px;text-align:justify;color:#555}
.welcome__btn{left:33px;top:120px;width:52px;height:17px;font-size:4.4px}
.welcome__photo{left:182px;top:20px;width:144px;height:116px;background:linear-gradient(120deg,#2b6fd0 0%,#5b8fd0 35%,#c89558 55%,#e2cfb2 80%,#f1efea 100%)}

/* services */
.services{background:linear-gradient(180deg,#e4e9ef,#eef1f5 60%,#e6eaf0)}
.page--a .services{height:213px}
.page--b .services{height:212px}
.sec-title{left:0;right:0;text-align:center;font-family:"Montserrat",sans-serif;font-weight:500;font-size:10px;color:var(--navy)}
.sec-rule{width:14px;height:1.2px;background:var(--navy);left:172px}
.svc-ring{left:0;top:0}
.svc-label{font-family:"Montserrat",sans-serif;font-weight:500;font-size:5px;color:#222}
.svc-text{font-size:3.7px;line-height:6.4px;color:#666;margin-top:3px}
.svc--left{text-align:right;width:70px}
.svc--right{text-align:left;width:70px}
.svc--center{text-align:center;width:80px;left:139px}
.ring-brand{left:139px;top:90px;width:80px;text-align:center;font-family:"Montserrat",sans-serif;font-weight:700;font-size:5.4px;color:var(--navy)}

/* shipping calculator */
.calc__title{font-family:"Montserrat",sans-serif;font-weight:500;font-size:9.6px;color:var(--navy);white-space:nowrap}
.calc__rule{width:14px;height:1.2px;background:var(--navy)}
.calc__input{height:17px;border:.6px solid #bbb;background:var(--white);font-size:3.9px;color:#666;display:flex;align-items:center;padding-left:7px}
.calc__fee{font-size:4.6px;font-weight:700;color:#333;white-space:nowrap}
.calc__note{font-size:3.8px;color:#555;line-height:7.4px}
.page--a .calc{height:138px}
.page--b .calc{height:159px}
.calc__boxes{background:linear-gradient(160deg,#e8d2ad,#d3ad76 55%,#c09560)}
.calc__port{left:0;top:0;width:174px;height:159px;background:linear-gradient(200deg,#f3b469 0%,#d9784a 25%,#586f88 55%,#1f4b5c 100%);clip-path:polygon(0 0,157px 0,174px 159px,0 159px)}

/* blog */
.page--a .blog{height:125px}
.page--b .blog{height:140px}
.card{width:144px;height:67px;border:.6px solid var(--line);background:var(--white)}
.card__photo{left:3px;top:3px;width:60px;height:61px}
.card__photo--a{background:linear-gradient(140deg,#6b5fb0,#c79a5e 55%,#8e6a3b)}
.card__photo--b{background:linear-gradient(170deg,#6b9ed8,#c5d8ea 55%,#c4c08a)}
.card__title{left:71px;top:8px;font-family:"Montserrat",sans-serif;font-size:5.2px;color:#222;white-space:nowrap}
.card__date{left:71px;top:19px;font-family:"Montserrat",sans-serif;font-size:4px;color:var(--orange)}
.card__text{left:71px;top:30px;width:66px;font-size:3.6px;line-height:7px;text-align:justify;color:#666}

/* contact */
.contact{height:163px;background:linear-gradient(180deg,#eef0f3,#e4e6ea 50%,#eceef1)}
.contact__sub{left:0;right:0;top:33px;text-align:center;font-size:4.6px;color:#444}
.field{background:var(--white);border:.5px solid #cfd3d8;font-size:3.9px;color:#555;padding:4px 5px}
.contact__submit{left:156px;top:121px;width:47px;height:16px;font-size:4.8px}
.phone{display:flex;align-items:center;gap:4px;font-size:3.9px;line-height:7px;color:#333;white-space:nowrap}

/* footer */
.site-footer{background:var(--navy-deep)}
.page--a .site-footer{height:104px}
.page--b .site-footer{height:105px}
.foot-brand{left:0;right:0;top:14px;text-align:center}
.foot-brand__name{font-family:"Montserrat",sans-serif;font-weight:700;font-size:7px;color:var(--orange)}
.foot-brand__sub{font-size:3.2px;letter-spacing:1.2px;color:var(--orange);margin-top:2px}
.foot-nav{left:0;right:0;top:54px;display:flex;justify-content:center;gap:15px;font-family:"Montserrat",sans-serif;font-weight:500;font-size:4px;color:var(--white)}
.socials{left:0;right:0;top:67px;display:flex;justify-content:center;gap:2px}
.socials span{width:11px;height:11px;border:.6px solid var(--white);border-radius:50%}
.copy{left:0;right:0;top:87px;text-align:center;font-family:"Montserrat",sans-serif;font-size:4.2px;color:var(--white)}
</style>
</head>
<body>

<!-- ===================== Concept A ===================== -->
<div class="page page--a">
  <header class="site-header">
    <div class="abs brand">
      <div class="brand__mark"><span class="brand__dot"></span><span class="brand__name">MAR-WICK SKY HARBOR</span></div>
      <div class="brand__sub">Custom Brokers Ltd.</div>
    </div>
    <p class="abs brand__addr">Shop 9 Birchfield Trade Centre, 227-229<br>Welland Avenue Kingston 8, Jamaica West Indies</p>
    <a class="abs btn btn--navy get-started">GET STARTED</a>
    <div class="abs call"><span class="ico-circle"><svg width="7" height="7" viewBox="0 0 24 24"><path fill="#fff" d="M6.6 10.8a15 15 0 0 0 6.6 6.6l2.2-2.2c.3-.3.7-.4 1-.2 1.1.4 2.3.6 3.6.6.6 0 1 .4 1 1V20c0 .6-.4 1-1 1A17 17 0 0 1 3 4c0-.6.4-1 1-1h3.5c.6 0 1 .4 1 1 0 1.3.2 2.5.6 3.6.1.3 0 .7-.2 1z"/></svg></span>CALL US : (876)555-0148</div>
    <nav class="abs nav"><span class="is-active">HOME</span><span>ABOUT US</span><span>SERVICES</span><span>NEWS</span><span>CONTACT US</span></nav>
  </header>

  <section class="hero" role="img" aria-label="Cargo plane over stacked containers and trucks, woman shopping online on a laptop">
    <div class="abs hero__shade"></div>
    <h1 class="abs hero__title">MAR-WICK SKY HARBOR</h1>
    <p class="abs hero__sub">SHOP ONLINE FROM THE USA AND SHIP TO JAMAICA</p>
    <a class="abs btn btn--orange hero__btn">REGISTER NOW</a>
  </section>

  <section class="welcome">
    <p class="abs welcome__kicker">WELCOME TO</p>
    <h2 class="abs welcome__title">MAR-WICK SKY HARBOR</h2>
    <p class="abs welcome__text">Sed ut perspiciatis unde omnis iste natus error sit voluptatem accusantium dol orem que laudantium, totam rem aperiam, eaque ipsa quae ab illo invent ore veritatis et quasi architecto beatae vitae dicta sunt explicabo. Nemo enim ipsam voluptatem quia volupt as sit aspernatur aut odit aut fugit, sed quia consequunt ur magni dolores eos qui ratione voluptatem sequi nesciunt.Neque porro quisquam est, qui dolorem ipsum quia dolor sit amet, consectetur, adipisci velit, sed quia non numquam eius modi tempora incidu nt ut labore et dolore magnam aliquam quaerat voluptatem.</p>
    <a class="abs btn btn--navy welcome__btn">READ MORE</a>
    <div class="abs welcome__photo" role="img" aria-label="Courier in a blue shirt handing a parcel to a customer"></div>
  </section>

  <section class="services">
    <h2 class="abs sec-title" style="top:15px">OUR <span class="accent">SERVICES</span></h2>
    <div class="abs sec-rule" style="top:31px"></div>
    <svg class="abs svc-ring" width="359" height="213" viewBox="0 0 359 213">
      <path d="M147 52 A55 55 0 1 0 214 52" fill="none" stroke="#13264c" stroke-width="1.3"/>
      <circle cx="147" cy="52" r="2.2" fill="#13264c"/><circle cx="214" cy="52" r="2.2" fill="#13264c"/>
      <circle cx="130" cy="74" r="12.5" fill="#e9a114"/>
      <circle cx="228" cy="74" r="12.5" fill="#e9a114"/>
      <circle cx="130" cy="119" r="12.5" fill="#13264c"/>
      <circle cx="228" cy="119" r="12.5" fill="#13264c"/>
      <circle cx="179" cy="149" r="12.5" fill="#e9a114"/>
      <g fill="none" stroke="#fff" stroke-width=".7" stroke-linejoin="round">
        <path d="M123 70h8v7h-8zM131 72h3l2 2.5v2.5h-5"/><circle cx="125.5" cy="78" r="1.2"/><circle cx="133" cy="78" r="1.2"/>
        <circle cx="228" cy="74" r="4"/><path d="M224 74h8M228 70v8"/>
        <path d="M124 115h5v8h-5zM129 120h4l2 3h-6"/><circle cx="131" cy="124" r="1"/>
        <path d="M222 116h7v8h-7zM226 120l7-5M233 115v3M233 115h-3"/>
        <path d="M174 144h6v10h-6zM180 147h5v7h-5zM175.5 147h3M175.5 150h3"/>
      </g>
    </svg>
    <div class="abs ring-brand">MAR-WICK SKY HARBOR</div>
    <div class="abs svc--left" style="left:42px;top:61px"><p class="svc-label">SHIPPING</p><p class="svc-text">Sed ut perspiciatis unde omnis<br>iste natus error</p></div>
    <div class="abs svc--right" style="left:248px;top:61px"><p class="svc-label">IMPORTS</p><p class="svc-text">Sed ut perspiciatis unde omnis<br>iste natus error</p></div>
    <div class="abs svc--left" style="left:42px;top:106px"><p class="svc-label">LOGISTICS</p><p class="svc-text">Sed ut perspiciatis unde omnis<br>iste natus error</p></div>
    <div class="abs svc--right" style="left:248px;top:106px"><p class="svc-label">EXPORT</p><p class="svc-text">Sed ut perspiciatis unde omnis<br>iste natus error</p></div>
    <div class="abs svc--center" style="top:164px"><p class="svc-label">CUSTOMS CLEARANCE</p><p class="svc-text">Sed ut perspiciatis unde omnis<br>iste natus error</p></div>
  </section>

  <section class="calc">
    <h2 class="abs calc__title" style="left:33px;top:20px">SHIPPING <span class="accent">CALCULATOR</span></h2>
    <div class="abs calc__rule" style="left:33px;top:37px"></div>
    <div class="abs calc__input" style="left:33px;top:46px;width:133px">Package Weight (lbs).......|</div>
    <p class="abs calc__fee" style="left:33px;top:71px">Estimated freight cost/courier fee is: $: <span class="accent">0 USD.</span></p>
    <p class="abs calc__note" style="left:33px;top:80px">(Based on weight of package only)</p>
    <p class="abs calc__note" style="left:33px;top:93px;width:140px">Packages <span class="accent">over $ 50.00 usd</span> in value are subjected to Custom charges. Please contact one of our offices for further details.</p>
    <div class="abs calc__boxes" style="left:190px;top:24px;width:130px;height:95px" role="img" aria-label="Stacked cardboard shipping boxes from online stores"></div>
  </section>

  <section class="blog">
    <h2 class="abs sec-title" style="top:9px">LATEST <span class="accent">BLOG</span></h2>
    <div class="abs sec-rule" style="top:25px"></div>
    <article class="abs card" style="left:33px;top:38px">
      <div class="abs card__photo card__photo--a" role="img" aria-label="Forklift with stacked boxes on a pallet"></div>
      <h3 class="abs card__title">Sed ut perspiciatis unde</h3>
      <p class="abs card__date">27 Nov 2020</p>
      <p class="abs card__text">Nemo enim ipsam voluptatem quia voluptas sit aspernatur aut odit aut fugit, sed quia consequuntur magni dolores eos qui ratione</p>
    </article>
    <article class="abs card" style="left:182px;top:38px">
      <div class="abs card__photo card__photo--b" role="img" aria-label="Worker in a hard hat guiding a container lift"></div>
      <h3 class="abs card__title">Sed ut perspiciatis unde</h3>
      <p class="abs card__date">27 Nov 2020</p>
      <p class="abs card__text">Nemo enim ipsam voluptatem quia voluptas sit aspernatur aut odit aut fugit, sed quia consequuntur magni dolores eos qui ratione</p>
    </article>
  </section>

  <section class="contact">
    <h2 class="abs sec-title" style="top:14px">CONTACT <span class="accent">US</span></h2>
    <p class="abs contact__sub">Creating Waves in the Logistic Industry.</p>
    <div class="abs field" style="left:84px;top:53px;width:94px;height:14px">First Name :</div>
    <div class="abs field" style="left:181px;top:53px;width:94px;height:14px">Last Name :</div>
    <div class="abs field" style="left:84px;top:70px;width:94px;height:14px">Email :</div>
    <div class="abs field" style="left:181px;top:70px;width:94px;height:14px">Phone :</div>
    <div class="abs field" style="left:84px;top:87px;width:191px;height:27px">Message :</div>
    <a class="abs btn btn--orange contact__submit">SUBMIT</a>
    <div class="abs phone" style="left:127px;top:141px"><span class="ico-circle"><svg width="7" height="7" viewBox="0 0 24 24"><path fill="#fff" d="M6.6 10.8a15 15 0 0 0 6.6 6.6l2.2-2.2c.3-.3.7-.4 1-.2 1.1.4 2.3.6 3.6.6.6 0 1 .4 1 1V20c0 .6-.4 1-1 1A17 17 0 0 1 3 4c0-.6.4-1 1-1h3.5c.6 0 1 .4 1 1 0 1.3.2 2.5.6 3.6.1.3 0 .7-.2 1z"/></svg></span><span>Phone :<br>(876)555-0172</span></div>
    <div class="abs phone" style="left:184px;top:141px"><span class="ico-circle"><svg width="7" height="7" viewBox="0 0 24 24"><path fill="#fff" d="M6.6 10.8a15 15 0 0 0 6.6 6.6l2.2-2.2c.3-.3.7-.4 1-.2 1.1.4 2.3.6 3.6.6.6 0 1 .4 1 1V20c0 .6-.4 1-1 1A17 17 0 0 1 3 4c0-.6.4-1 1-1h3.5c.6 0 1 .4 1 1 0 1.3.2 2.5.6 3.6.1.3 0 .7-.2 1z"/></svg></span><span>Phone :<br>(876)555-0148</span></div>
  </section>

  <footer class="site-footer">
    <div class="abs foot-brand"><p class="foot-brand__name">MAR-WICK SKY HARBOR</p><p class="foot-brand__sub">Custom Brokers Ltd.</p></div>
    <nav class="abs foot-nav"><span>HOME</span><span>ABOUT US</span><span>SERVICES</span><span>NEWS</span><span>CONTACT US</span></nav>
    <div class="abs socials"><span></span><span></span><span></span><span></span><span></span></div>
    <p class="abs copy">©2020 Marwick Sky Harbor.All rights reserved.</p>
  </footer>
</div>

<!-- ===================== Concept B ===================== -->
<div class="page page--b">
  <header class="site-header">
    <div class="abs brand">
      <div class="brand__mark"><span class="brand__dot"></span><span class="brand__name">MAR-WICK SKY HARBOR</span></div>
      <div class="brand__sub">Custom Brokers Ltd.</div>
    </div>
    <p class="abs brand__addr">Shop 9 Birchfield Trade Centre, 227-229<br>Welland Avenue Kingston 8, Jamaica West Indies</p>
    <a class="abs btn btn--navy get-started">GET STARTED</a>
    <div class="abs call"><span class="ico-circle"><svg width="7" height="7" viewBox="0 0 24 24"><path fill="#fff" d="M6.6 10.8a15 15 0 0 0 6.6 6.6l2.2-2.2c.3-.3.7-.4 1-.2 1.1.4 2.3.6 3.6.6.6 0 1 .4 1 1V20c0 .6-.4 1-1 1A17 17 0 0 1 3 4c0-.6.4-1 1-1h3.5c.6 0 1 .4 1 1 0 1.3.2 2.5.6 3.6.1.3 0 .7-.2 1z"/></svg></span>CALL US : (876)555-0148</div>
    <nav class="abs nav"><span class="is-active">HOME</span><span>ABOUT US</span><span>SERVICES</span><span>NEWS</span><span>CONTACT US</span></nav>
  </header>

  <section class="hero" role="img" aria-label="Cargo plane over stacked containers and trucks, woman shopping online on a laptop">
    <div class="abs hero__shade"></div>
    <h1 class="abs hero__title">MAR-WICK SKY HARBOR</h1>
    <p class="abs hero__sub">SHOP ONLINE FROM THE USA AND SHIP TO JAMAICA</p>
    <a class="abs btn btn--orange hero__btn">REGISTER NOW</a>
  </section>

  <section class="welcome">
    <p class="abs welcome__kicker">WELCOME TO</p>
    <h2 class="abs welcome__title">MAR-WICK SKY HARBOR</h2>
    <p class="abs welcome__text">Sed ut perspiciatis unde omnis iste natus error sit voluptatem accusantium dol orem que laudantium, totam rem aperiam, eaque ipsa quae ab illo invent ore veritatis et quasi architecto beatae vitae dicta sunt explicabo. Nemo enim ipsam voluptatem quia volupt as sit aspernatur aut odit aut fugit, sed quia consequunt ur magni dolores eos qui ratione voluptatem sequi nesciunt.Neque porro quisquam est, qui dolorem ipsum quia dolor sit amet, consectetur, adipisci velit, sed quia non numquam eius modi tempora incidu nt ut labore et dolore magnam aliquam quaerat voluptatem.</p>
    <a class="abs btn btn--navy welcome__btn">READ MORE</a>
    <div class="abs welcome__photo" role="img" aria-label="Courier in a blue shirt handing a parcel to a customer"></div>
  </section>

  <section class="services">
    <h2 class="abs sec-title" style="top:15px">OUR <span class="accent">SERVICES</span></h2>
    <div class="abs sec-rule" style="top:31px"></div>
    <svg class="abs svc-ring" width="359" height="212" viewBox="0 0 359 212">
      <path d="M147 52 A55 55 0 1 0 214 52" fill="none" stroke="#13264c" stroke-width="1.3"/>
      <circle cx="147" cy="52" r="2.2" fill="#13264c"/><circle cx="214" cy="52" r="2.2" fill="#13264c"/>
      <circle cx="130" cy="74" r="12.5" fill="#e9a114"/>
      <circle cx="228" cy="74" r="12.5" fill="#e9a114"/>
      <circle cx="130" cy="119" r="12.5" fill="#13264c"/>
      <circle cx="228" cy="119" r="12.5" fill="#13264c"/>
      <circle cx="179" cy="149" r="12.5" fill="#e9a114"/>
      <g fill="none" stroke="#fff" stroke-width=".7" stroke-linejoin="round">
        <path d="M123 70h8v7h-8zM131 72h3l2 2.5v2.5h-5"/><circle cx="125.5" cy="78" r="1.2"/><circle cx="133" cy="78" r="1.2"/>
        <circle cx="228" cy="74" r="4"/><path d="M224 74h8M228 70v8"/>
        <path d="M124 115h5v8h-5zM129 120h4l2 3h-6"/><circle cx="131" cy="124" r="1"/>
        <path d="M222 116h7v8h-7zM226 120l7-5M233 115v3M233 115h-3"/>
        <path d="M174 144h6v10h-6zM180 147h5v7h-5zM175.5 147h3M175.5 150h3"/>
      </g>
    </svg>
    <div class="abs ring-brand">MAR-WICK SKY HARBOR</div>
    <div class="abs svc--left" style="left:42px;top:61px"><p class="svc-label">SHIPPING</p><p class="svc-text">Sed ut perspiciatis unde omnis<br>iste natus error</p></div>
    <div class="abs svc--right" style="left:248px;top:61px"><p class="svc-label">IMPORTS</p><p class="svc-text">Sed ut perspiciatis unde omnis<br>iste natus error</p></div>
    <div class="abs svc--left" style="left:42px;top:106px"><p class="svc-label">LOGISTICS</p><p class="svc-text">Sed ut perspiciatis unde omnis<br>iste natus error</p></div>
    <div class="abs svc--right" style="left:248px;top:106px"><p class="svc-label">EXPORT</p><p class="svc-text">Sed ut perspiciatis unde omnis<br>iste natus error</p></div>
    <div class="abs svc--center" style="top:164px"><p class="svc-label">CUSTOMS CLEARANCE</p><p class="svc-text">Sed ut perspiciatis unde omnis<br>iste natus error</p></div>
  </section>

  <section class="calc">
    <div class="abs calc__port" role="img" aria-label="Container ship sailing at sunset beside a port"></div>
    <h2 class="abs calc__title" style="left:181px;top:18px">SHIPPING <span class="accent">CALCULATOR</span></h2>
    <div class="abs calc__rule" style="left:181px;top:34px"></div>
    <div class="abs calc__input" style="left:181px;top:43px;width:133px">Package Weight (lbs).......|</div>
    <p class="abs calc__fee" style="left:181px;top:67px">Estimated freight cost/courier fee is: $: <span class="accent">0 USD.</span></p>
    <p class="abs calc__note" style="left:181px;top:76px">(Based on weight of package only)</p>
    <p class="abs calc__note" style="left:181px;top:89px;width:104px">Packages <span class="accent">over $ 50.00 usd</span> in value are subjected to Custom charges.Please contact one of our offices for further details.</p>
    <div class="abs calc__boxes" style="left:287px;top:88px;width:66px;height:62px" role="img" aria-label="Stacked cardboard shipping boxes from online stores"></div>
  </section>

  <section class="blog">
    <h2 class="abs sec-title" style="top:25px">LATEST <span class="accent">BLOG</span></h2>
    <div class="abs sec-rule" style="top:41px"></div>
    <article class="abs card" style="left:33px;top:54px">
      <div class="abs card__photo card__photo--a" role="img" aria-label="Forklift with stacked boxes on a pallet"></div>
      <h3 class="abs card__title">Sed ut perspiciatis unde</h3>
      <p class="abs card__date">27 Nov 2020</p>
      <p class="abs card__text">Nemo enim ipsam voluptatem quia voluptas sit aspernatur aut odit aut fugit, sed quia consequuntur magni dolores eos qui ratione</p>
    </article>
    <article class="abs card" style="left:182px;top:54px">
      <div class="abs card__photo card__photo--b" role="img" aria-label="Worker in a hard hat guiding a container lift"></div>
      <h3 class="abs card__title">Sed ut perspiciatis unde</h3>
      <p class="abs card__date">27 Nov 2020</p>
      <p class="abs card__text">Nemo enim ipsam voluptatem quia voluptas sit aspernatur aut odit aut fugit, sed quia consequuntur magni dolores eos qui ratione</p>
    </article>
  </section>

  <section class="contact">
    <h2 class="abs sec-title" style="top:14px">CONTACT <span class="accent">US</span></h2>
    <p class="abs contact__sub">Creating Waves in the Logistic Industry.</p>
    <div class="abs field" style="left:84px;top:53px;width:94px;height:14px">First Name :</div>
    <div class="abs field" style="left:181px;top:53px;width:94px;height:14px">Last Name :</div>
    <div class="abs field" style="left:84px;top:70px;width:94px;height:14px">Email :</div>
    <div class="abs field" style="left:181px;top:70px;width:94px;height:14px">Phone :</div>
    <div class="abs field" style="left:84px;top:87px;width:191px;height:27px">Message :</div>
    <a class="abs btn btn--orange contact__submit">SUBMIT</a>
    <div class="abs phone" style="left:127px;top:141px"><span class="ico-circle"><svg width="7" height="7" viewBox="0 0 24 24"><path fill="#fff" d="M6.6 10.8a15 15 0 0 0 6.6 6.6l2.2-2.2c.3-.3.7-.4 1-.2 1.1.4 2.3.6 3.6.6.6 0 1 .4 1 1V20c0 .6-.4 1-1 1A17 17 0 0 1 3 4c0-.6.4-1 1-1h3.5c.6 0 1 .4 1 1 0 1.3.2 2.5.6 3.6.1.3 0 .7-.2 1z"/></svg></span><span>Phone :<br>(876)555-0172</span></div>
    <div class="abs phone" style="left:184px;top:141px"><span class="ico-circle"><svg width="7" height="7" viewBox="0 0 24 24"><path fill="#fff" d="M6.6 10.8a15 15 0 0 0 6.6 6.6l2.2-2.2c.3-.3.7-.4 1-.2 1.1.4 2.3.6 3.6.6.6 0 1 .4 1 1V20c0 .6-.4 1-1 1A17 17 0 0 1 3 4c0-.6.4-1 1-1h3.5c.6 0 1 .4 1 1 0 1.3.2 2.5.6 3.6.1.3 0 .7-.2 1z"/></svg></span><span>Phone :<br>(876)555-0148</span></div>
  </section>

  <footer class="site-footer">
    <div class="abs foot-brand"><p class="foot-brand__name">MAR-WICK SKY HARBOR</p><p class="foot-brand__sub">Custom Brokers Ltd.</p></div>
    <nav class="abs foot-nav"><span>HOME</span><span>ABOUT US</span><span>SERVICES</span><span>NEWS</span><span>CONTACT US</span></nav>
    <div class="abs socials"><span></span><span></span><span></span><span></span><span></span></div>
    <p class="abs copy">©2020 Marwick Sky Harbor.All rights reserved.</p>
  </footer>
</div>

</body>
</html>
```